KR business cards
Business cards for Consulting outfit
Project: KR business cards
KR business cards -
Creative Brief
Professional
No name
No address
info@vosk-lantern.example
vosk-lantern.example
Would like business cards for 8 different people. No address on the card
Logo + We define the standard

```html
<!DOCTYPE html>
<html lang="en">
<head>
<meta charset="utf-8">
<title>vosk-lantern stationery</title>
<link href="https://fonts.googleapis.com/css2?family=Lora:wght@400&family=Open+Sans:wght@400;600&display=swap" rel="stylesheet">
<style>
  :root {
    --stage: #2f2f2f;
    --paper: #ffffff;
    --paper-edge: #e6e6e6;
    --brand-red: #c4202b;
    --flap-grey: #6e6666;
    --ink: #4a4a4a;
    --ink-soft: #9a9a9a;
    --label: #8a8a8a;
  }
  * { box-sizing: border-box; margin: 0; padding: 0; }
  html, body { width: 1200px; height: 307px; overflow: hidden; }
  body {
    background: var(--stage);
    position: relative;
    font-family: "Open Sans", Arial, sans-serif;
    color: var(--ink);
  }
  .piece { position: absolute; background: var(--paper); }
  .wordmark {
    font-family: "Lora", Georgia, serif;
    font-weight: 400;
    color: var(--brand-red);
    white-space: nowrap;
    display: flex;
    align-items: center;
    gap: 4px;
  }
  .wordmark .mark-square { display: inline-block; background: currentColor; }
  .label {
    position: absolute;
    font-size: 4px;
    color: var(--label);
    text-align: center;
    width: 100%;
    bottom: -9px;
    left: 0;
  }

  /* Brand lockup on the stage */
  .brand-lockup { position: absolute; left: 14px; top: 26px; width: 180px; text-align: center; }
  .brand-lockup .wordmark { color: var(--paper); font-size: 26px; justify-content: center; }
  .brand-lockup .wordmark .mark-square { width: 12px; height: 12px; background: var(--brand-red); }
  .brand-lockup .tagline { color: #cfcfcf; font-size: 6px; letter-spacing: 0.5px; margin-top: 4px; }

  /* Business cards */
  .card { width: 102px; height: 56px; display: flex; align-items: center; justify-content: center; }
  .card .wordmark { font-size: 10px; }
  .card .wordmark .mark-square { width: 5px; height: 5px; }
  .card-front { left: 12px; top: 112px; }
  .card-back { left: 125px; top: 112px; display: block; padding: 8px 9px; border-left: 4px solid var(--brand-red); }
  .card-back .person { font-size: 5px; font-weight: 600; color: var(--brand-red); }
  .card-back .role { font-size: 3.6px; color: var(--ink-soft); margin-bottom: 10px; }
  .card-back .contact { font-size: 3.6px; line-height: 1.5; }
  .card-plain { left: 12px; top: 208px; }
  .card-red { left: 125px; top: 208px; background: var(--brand-red); }
  .card-red .wordmark { color: var(--paper); }

  /* Letterheads */
  .letterhead { width: 212px; height: 264px; top: 24px; }
  .letterhead .head { position: absolute; left: 16px; top: 14px; }
  .letterhead .wordmark { font-size: 9px; }
  .letterhead .wordmark .mark-square { width: 5px; height: 5px; }
  .letterhead .tab { position: absolute; top: 0; left: 0; width: 5px; height: 22px; background: var(--brand-red); }
  .letterhead .foot {
    position: absolute; bottom: 10px; left: 0; width: 100%;
    text-align: center; font-size: 3.6px; color: var(--ink-soft);
  }
  .letterhead-front { left: 245px; }
  .letterhead-back { left: 480px; }

  /* Compliment slips */
  .slip { width: 204px; height: 98px; left: 696px; }
  .slip .tab { position: absolute; left: 0; top: 0; width: 5px; height: 18px; background: var(--brand-red); }
  .slip .head { position: absolute; left: 14px; top: 12px; }
  .slip .wordmark { font-size: 8px; }
  .slip .wordmark .mark-square { width: 4px; height: 4px; }
  .slip .foot { position: absolute; bottom: 8px; width: 100%; text-align: center; font-size: 3.4px; color: var(--ink-soft); }
  .slip-top { top: 24px; }
  .slip-bottom { top: 182px; }

  /* Envelopes */
  .envelope { width: 222px; height: 72px; left: 955px; overflow: hidden; border: 1px solid var(--paper-edge); }
  .envelope svg { position: absolute; inset: 0; }
  .envelope-grey { top: 58px; }
  .envelope-red { top: 138px; }
  .envelope-white { top: 212px; }
  .envelope .wordmark { position: absolute; left: 10px; top: 8px; font-size: 7px; }
  .envelope .wordmark .mark-square { width: 4px; height: 4px; }
</style>
</head>
<body>

  <header class="brand-lockup">
    <div class="wordmark"><span class="mark-square"></span>vosk-lantern</div>
    <p class="tagline">We define the standard</p>
  </header>

  <!-- Business cards -->
  <section class="piece card card-front">
    <div class="wordmark"><span class="mark-square"></span>vosk-lantern</div>
  </section>
  <section class="piece card card-back">
    <p class="person">Name Surname</p>
    <p class="role">Consultant</p>
    <p class="contact">info@vosk-lantern.example<br>vosk-lantern.example</p>
  </section>
  <section class="piece card card-plain">
    <div class="wordmark"><span class="mark-square"></span>vosk-lantern</div>
    <span class="label">Business cards</span>
  </section>
  <section class="piece card card-red">
    <div class="wordmark"><span class="mark-square"></span>vosk-lantern</div>
  </section>

  <!-- Letterheads -->
  <section class="piece letterhead letterhead-front">
    <span class="tab"></span>
    <div class="head"><div class="wordmark"><span class="mark-square"></span>vosk-lantern</div></div>
    <p class="foot">info@vosk-lantern.example &nbsp;|&nbsp; vosk-lantern.example</p>
    <span class="label">Letterhead front</span>
  </section>
  <section class="piece letterhead letterhead-back">
    <span class="tab"></span>
    <div class="head"><div class="wordmark"><span class="mark-square"></span>vosk-lantern</div></div>
    <p class="foot">info@vosk-lantern.example &nbsp;|&nbsp; vosk-lantern.example</p>
    <span class="label">Letterhead back</span>
  </section>

  <!-- Compliment slips -->
  <section class="piece slip slip-top">
    <span class="tab"></span>
    <div class="head"><div class="wordmark"><span class="mark-square"></span>vosk-lantern</div></div>
    <p class="foot">info@vosk-lantern.example &nbsp;|&nbsp; vosk-lantern.example</p>
  </section>
  <section class="piece slip slip-bottom">
    <span class="tab"></span>
    <div class="head"><div class="wordmark"><span class="mark-square"></span>vosk-lantern</div></div>
    <p class="foot">info@vosk-lantern.example &nbsp;|&nbsp; vosk-lantern.example</p>
    <span class="label">Compliment slip</span>
  </section>

  <!-- Envelopes -->
  <section class="piece envelope envelope-grey">
    <svg width="222" height="72" viewBox="0 0 222 72" aria-hidden="true">
      <polygon points="0,0 222,0 222,10 111,40 0,10" fill="var(--flap-grey)"/>
    </svg>
  </section>
  <section class="piece envelope envelope-red">
    <svg width="222" height="72" viewBox="0 0 222 72" aria-hidden="true">
      <polygon points="0,0 222,0 111,34" fill="var(--brand-red)"/>
    </svg>
  </section>
  <section class="piece envelope envelope-white">
    <svg width="222" height="72" viewBox="0 0 222 72" aria-hidden="true">
      <polyline points="0,0 111,36 222,0" fill="none" stroke="var(--paper-edge)" stroke-width="1"/>
    </svg>
    <div class="wordmark"><span class="mark-square"></span>vosk-lantern</div>
    <span class="label">Envelope DL</span>
  </section>

</body>
</html>
```